Simple and Clean business card design

We would like the design to be simple clean and to incorporate our colors.

We are open to your design and talent, we have the dots in our logo as we think of it as data points and we connect data points for people.

We are open to see the great creative and clean design you bring to the table

Contact Information for Business Card

please include: name, position, email, phone and website

Font styles to use
Sans Serif

Requirements
Must have
• my colors incorporated, simplicity
Nice to have
• lots of white space, simplicity
Should not have
• complexicity/ complex art

```html
<!DOCTYPE html>
<html lang="en">
<head>
<meta charset="utf-8">
<title>Spora business card</title>
<link href="https://fonts.googleapis.com/css2?family=Work+Sans:wght@400;500;600&display=swap" rel="stylesheet">
<style>
  :root {
    --stage: #1c1c1c;
    --card: #232323;
    --ink: #ffffff;
    --silver: #cfcfcf;
    --blue: #5b80c4;
    --green: #3aa655;
    --yellow: #f5be24;
    --red: #e8493c;
  }
  * { margin: 0; padding: 0; box-sizing: border-box; }
  html, body {
    width: 1200px; height: 900px; overflow: hidden;
    background: var(--stage);
    font-family: "Work Sans", Arial, sans-serif;
  }
  .stage {
    position: relative; width: 1200px; height: 900px;
    display: flex; flex-direction: column; align-items: center;
    justify-content: center; gap: 24px;
  }
  .card {
    position: relative; width: 700px; height: 400px;
    background: var(--card);
    box-shadow: 0 10px 30px rgba(0,0,0,.5);
  }
  .card-back { display: flex; align-items: center; justify-content: center; }
  .wordmark {
    display: flex; align-items: center; gap: 14px;
    font-weight: 500; letter-spacing: 1px; line-height: 1;
  }
  .wordmark-dot { border-radius: 50%; background: var(--blue); flex: none; }
  .card-back .wordmark { font-size: 104px; color: var(--silver); }
  .card-back .wordmark-dot { width: 26px; height: 26px; }
  .card-front .wordmark {
    position: absolute; left: 60px; top: 52px;
    font-size: 74px; color: var(--ink);
  }
  .card-front .wordmark-dot { width: 20px; height: 20px; }
  .contact-block {
    position: absolute; left: 60px; top: 172px;
    padding-left: 28px; color: var(--ink);
  }
  .accent-bar {
    position: absolute; left: 0; top: 4px;
    width: 10px; height: 44px; background: var(--yellow);
  }
  .person-name {
    font-size: 29px; font-weight: 500; color: var(--blue);
    letter-spacing: 3px; text-transform: uppercase; line-height: 1.1;
  }
  .person-role { font-size: 19px; margin-top: 2px; }
  .address { font-size: 19px; line-height: 1.35; margin-top: 16px; }
  .contact-list { list-style: none; margin-top: 10px; font-size: 20px; line-height: 1.45; }
  .contact-list li { display: flex; align-items: center; gap: 10px; }
  .contact-list svg { width: 16px; height: 16px; flex: none; }
</style>
</head>
<body>
<main class="stage">
  <section class="card card-back" aria-label="Card back">
    <div class="wordmark"><span>Spora</span><span class="wordmark-dot"></span></div>
  </section>

  <section class="card card-front" aria-label="Card front">
    <div class="wordmark"><span>Spora</span><span class="wordmark-dot"></span></div>
    <div class="contact-block">
      <span class="accent-bar"></span>
      <p class="person-name">Daniel Reyes</p>
      <p class="person-role">Founder</p>
      <p class="address">418 Cedar Bend Lane<br>Marfield, TX 78012</p>
      <ul class="contact-list">
        <li>
          <svg viewBox="0 0 16 16" aria-hidden="true"><path d="M4 1l3 3-2 2c1 2 3 4 5 5l2-2 3 3-2 3C7 15 1 9 1 3z" fill="var(--blue)"/></svg>
          0412 555 019
        </li>
        <li>
          <svg viewBox="0 0 16 16" aria-hidden="true"><rect x="1.5" y="3.5" width="13" height="9" fill="none" stroke="var(--blue)" stroke-width="1.4"/><path d="M1.5 3.5l6.5 5 6.5-5" fill="none" stroke="var(--blue)" stroke-width="1.4"/></svg>
          hello@sporadata.com
        </li>
        <li>
          <svg viewBox="0 0 16 16" aria-hidden="true"><g fill="none" stroke="var(--blue)" stroke-width="1.3"><circle cx="8" cy="8" r="6.5"/><ellipse cx="8" cy="8" rx="3" ry="6.5"/><path d="M1.5 8h13M2.5 4.8h11M2.5 11.2h11"/></g></svg>
          www.sporadata.com
        </li>
      </ul>
    </div>
  </section>
</main>
</body>
</html>
```